47certo.com - International Brand Needs A Fresh Look

New Company needing an fresh clean look. 47certos.com.au

Product: SSLs

Brands: Corvalix, TerraLok, Brindle, SwiftKey

Encourage all designers that can deliver a clean and fresh design with a touch of imagination.

We don't want this to be your typical boring ssl reseller site, we want the whole process to be fast and transparent. We welcome your design ideas.

Unrelated site designs we like:
www.plumvendor.com, www.flonter.com

Backend - Quillbase Run

Pages to design:

Home Page - see examples above. looking for fresh ideas!!

Product Page - try and avoid grids or boring/usual ways to display ssl information and product info. looking for fresh ideas!!

Contact us page

Checkout - using quillbase run, so not sure how much we can customise on this page

we had thought about an idea using an input box on the home page - that looks like a browser bar where they enter the url they are purchasing for - different way to display this and get them to interact with the site. when they click find SSLs button the options display below.... just a thought!

Please ask any questions you have.

Thanks.
Marcus

Industry/Entity Type

It Company

Requirements
Must have
• logos of the brands we are selling and we are platinum partners of each.

logo's of brands that use our ssls - please choose some example ones.

Nice to have
• nice to have a most popular either for each one or across the site

```html
<!DOCTYPE html>
<html lang="en">
<head>
<meta charset="utf-8">
<title>47certo – SSL Certificates</title>
<link href="https://fonts.googleapis.com/css2?family=Varela+Round&family=Questrial&family=Arimo:wght@400;700&display=swap" rel="stylesheet">
<style>
:root{
  --ink:#1b1b1b;
  --topbar:#0b0b0b;
  --navbar:#1f1f1f;
  --cyan:#3fb8e0;
  --why:#4ac3e6;
  --what:#1aa5cf;
  --org:#06c489;
  --ext:#ea9a2b;
  --ext-label:#fde2b6;
  --green:#7bc943;
  --green-dark:#5ea62c;
  --red:#b01e24;
  --yellow:#ffe23a;
  --strip:#f2f2f2;
  --footer:#262626;
  --muted:#9a9a9a;
  --white:#ffffff;
}
*{box-sizing:border-box;margin:0;padding:0}
html,body{width:1200px;height:3165px;overflow:hidden;background:var(--white)}
body{font-family:"Arimo",Arial,sans-serif;color:var(--ink);position:relative}
.display{font-family:"Varela Round","Questrial",sans-serif}
.abs{position:absolute}

/* Top bar */
.topbar{position:absolute;left:0;top:0;width:1200px;height:63px;background:var(--topbar)}
.brand{position:absolute;left:153px;top:10px;font-family:"Varela Round",sans-serif;font-size:40px;color:var(--cyan);letter-spacing:-1px}
.regions{position:absolute;left:680px;top:23px;font-size:13px;color:#bdbdbd}
.regions .flag{display:inline-block;width:18px;height:11px;background:#c9c9d6;margin-left:6px;vertical-align:-1px}
.search{position:absolute;left:786px;top:21px;width:242px;height:24px;background:var(--white)}
.search svg{position:absolute;right:6px;top:5px}

/* Nav */
.navbar{position:absolute;left:0;top:63px;width:1200px;height:58px;background:var(--navbar)}
.navbar ul{list-style:none;position:absolute;right:134px;top:19px;display:flex;gap:0}
.navbar li{color:var(--white);font-size:17px;margin-left:44px}

/* Hero */
.hero-title{position:absolute;left:0;width:1200px;top:222px;text-align:center;font-size:78px;line-height:80px;color:var(--cyan);letter-spacing:-1px}
.hero-sub{position:absolute;left:0;width:1200px;top:403px;text-align:center;font-family:"Questrial",sans-serif;font-size:27px;line-height:42px;color:#222}
.url-input{position:absolute;left:256px;top:527px;width:477px;height:64px;background:#e7e7e7;border:2px solid #d4d4d4;border-radius:8px;font-family:"Questrial",sans-serif;font-size:22px;color:#8a8a8a;padding:18px 26px}
.find-btn{position:absolute;left:746px;top:527px;width:198px;height:64px;border-radius:8px;background:linear-gradient(var(--green),var(--green-dark));color:var(--white);font-family:"Questrial",sans-serif;font-size:23px;text-align:center;line-height:64px}

/* Why */
.why{position:absolute;left:0;top:704px;width:1200px;height:472px;background:var(--why)}
.why h2{position:absolute;left:0;width:1200px;top:72px;text-align:center;font-size:86px;color:var(--white);font-weight:400}
.feature{position:absolute;top:210px;width:300px;text-align:center}
.feature svg{display:block;margin:0 auto}
.feature h3{font-size:24px;margin-top:24px;color:var(--ink)}
.feature p{font-size:16px;line-height:24px;margin-top:12px;color:#13343f}

/* Trial */
.trial-photo{position:absolute;left:163px;top:1213px;width:417px;height:493px;background:linear-gradient(180deg,#f2f2f2 0%,#e6d2c2 30%,#d23a33 62%,#c9302b 100%)}
.bubble{position:absolute;left:119px;top:1405px}
.bubble-text{position:absolute;left:150px;top:1455px;width:345px;text-align:center;color:var(--white);font-family:"Questrial",sans-serif;font-size:31px;line-height:38px;font-weight:700}
.bubble-text em{font-style:normal;color:var(--yellow)}
.trial-copy{position:absolute;left:620px;top:1298px;width:340px}
.trial-copy h2{font-family:"Questrial",sans-serif;font-size:42px;color:var(--red);font-weight:700}
.trial-copy h3{font-size:20px;margin-top:22px}
.trial-copy p{font-size:15px;line-height:20px;margin-top:14px;color:#222}

/* What you get */
.what{position:absolute;left:0;top:1706px;width:1200px;height:456px;background:var(--what)}
.what h2{position:absolute;left:0;width:1200px;top:50px;text-align:center;font-size:72px;color:var(--white);font-weight:400}
.what .rule{position:absolute;left:190px;top:174px;width:820px;height:1px;background:#5cc3e2}
.band{position:absolute;left:0;width:1200px}
.band-org{top:2162px;height:280px;background:var(--org)}
.band-ext{top:2442px;height:300px;background:var(--ext)}
.notch{position:absolute;left:559px;top:0}
.tier-label{position:absolute;right:768px;text-align:right;font-family:"Questrial",sans-serif;font-size:40px;line-height:48px;color:var(--white);font-weight:700}
.tier-body{position:absolute;left:488px;width:500px}
.tier-body h3{font-size:20px;color:var(--ink)}
.tier-body p{font-size:15px;line-height:22px;margin-top:8px;color:var(--white)}
.learn-btn{display:block;width:187px;height:45px;margin-top:12px;background:var(--white);border-radius:5px;text-align:center;line-height:45px;font-size:18px;color:#222}

/* Clients */
.clients{position:absolute;left:0;top:2742px;width:1200px;height:154px;background:var(--strip)}
.client{position:absolute;top:64px;font-size:22px;font-weight:700;color:#333;transform:translateX(-50%);white-space:nowrap}
.client .dot{display:inline-block;width:14px;height:14px;background:#333;margin-right:8px;vertical-align:0}

/* Footer */
.footer{position:absolute;left:0;top:2896px;width:1200px;height:269px;background:var(--footer);color:var(--white)}
.footer .mark{position:absolute;left:190px;top:76px;font-family:"Varela Round",sans-serif;font-size:40px;color:var(--muted)}
.footer .links{position:absolute;left:190px;top:143px;font-size:16px}
.footer .links span{margin:0 10px}
.footer .copy{position:absolute;left:190px;top:168px;font-size:14px;color:#d8d8d8}
.footer .contact{position:absolute;right:180px;top:68px;text-align:right;font-size:16px;line-height:22px}
.footer .address{position:absolute;right:180px;top:148px;text-align:right;font-size:16px;line-height:22px}
</style>
</head>
<body>

<header class="topbar">
  <div class="brand">47certo</div>
  <div class="regions">Regions<span class="flag"></span></div>
  <div class="search">
    <svg width="14" height="14" viewBox="0 0 14 14"><circle cx="5.5" cy="5.5" r="4" fill="none" stroke="#111" stroke-width="2"/><line x1="8.5" y1="8.5" x2="13" y2="13" stroke="#111" stroke-width="2"/></svg>
  </div>
</header>
<nav class="navbar">
  <ul><li>Products</li><li>Partners</li><li>Support</li><li>Resources</li><li>SignIn</li></ul>
</nav>

<section>
  <h1 class="hero-title display">Protect Your Website<br>&amp; Grow Your Business</h1>
  <p class="hero-sub">Check out our new reduced prices on organization<br>and extended validation SSL!</p>
  <div class="url-input">Enter your website here</div>
  <div class="find-btn">Find SSLs</div>
</section>

<section class="why">
  <h2 class="display">Why choose 47certo?</h2>
  <div class="feature" style="left:145px">
    <svg width="54" height="66" viewBox="0 0 54 66"><path d="M17 20 V12 a10 10 0 0 1 20 0 V20" fill="none" stroke="#fff" stroke-width="4"/><rect x="4" y="20" width="46" height="44" rx="3" fill="#fff"/><text x="27" y="51" text-anchor="middle" font-family="Arimo,sans-serif" font-size="22" fill="#4ac3e6">$</text></svg>
    <h3>Fixed Pricing</h3>
    <p>Find out what you will pay up front.<br>No hidden surprises.</p>
  </div>
  <div class="feature" style="left:435px">
    <svg width="60" height="66" viewBox="0 0 60 66"><rect x="24" y="2" width="12" height="7" fill="#fff"/><circle cx="30" cy="38" r="24" fill="none" stroke="#fff" stroke-width="5"/><line x1="30" y1="38" x2="30" y2="22" stroke="#fff" stroke-width="4"/><line x1="30" y1="38" x2="42" y2="44" stroke="#fff" stroke-width="4"/></svg>
    <h3>Money back guarantee</h3>
    <p>We're here when you've got an urgent<br>project you need turned around fast.</p>
  </div>
  <div class="feature" style="left:762px">
    <svg width="60" height="66" viewBox="0 0 60 66"><path d="M14 4 H46 V24 a16 16 0 0 1 -32 0 Z" fill="#fff"/><path d="M14 10 H4 V18 a10 10 0 0 0 10 10 M46 10 H56 V18 a10 10 0 0 1 -10 10" fill="none" stroke="#fff" stroke-width="4"/><rect x="26" y="40" width="8" height="12" fill="#fff"/><rect x="16" y="52" width="28" height="10" fill="#fff"/></svg>
    <h3>We are the best</h3>
    <p>We didn't become #1 by accident.<br>Just ask our customers.</p>
  </div>
</section>

<section>
  <div class="trial-photo" role="img" aria-label="Photo of a smiling man in a red T-shirt holding up a speech-bubble sign"></div>
  <svg class="bubble" width="420" height="210" viewBox="0 0 420 210"><path d="M30 10 H390 Q410 10 410 30 V150 Q410 170 390 170 H120 L70 205 L80 170 H30 Q10 170 10 150 V30 Q10 10 30 10 Z" fill="#56a845"/></svg>
  <div class="bubble-text">Get a <em>Free 30-Day</em><br>SSL Trial Certificate</div>
  <div class="trial-copy">
    <h2>Try it NOW!</h2>
    <h3>Try before you buy...for free</h3>
    <p>The free* 47certo® SSL Trial offers a fully functioning SSL certificate. Now you can make a true evaluation of your SSL needs before you purchase.</p>
    <p>TerraLok SSL certificates help ensure that your customers' and business partners' information is secure when they use your site. Secure your site in minutes with the TerraLok SSL Trial certificate, enabling up to 256-bit encryption.*</p>
  </div>
</section>

<section class="what">
  <h2 class="display">What you get from 47certo</h2>
  <div class="rule"></div>
  <svg class="abs" style="left:559px;top:174px" width="52" height="26" viewBox="0 0 52 26"><path d="M0 0 H52 L26 26 Z" fill="#127f9f"/></svg>
  <div class="tier-label" style="top:290px">Domain<br>SSL</div>
  <div class="tier-body" style="top:250px">
    <h3>Fast &amp; Economical</h3>
    <p>Quick issuance SSL Certificate &amp; Secure Site Seal. SSL without any paperwork or fuss &amp; delivered in minutes!</p>
    <span class="learn-btn">Learn More</span>
  </div>
</section>

<section class="band band-org">
  <svg class="notch" width="52" height="26" viewBox="0 0 52 26"><path d="M0 0 H52 L26 26 Z" fill="var(--what)"/></svg>
  <div class="tier-label" style="top:90px;font-size:39px">Organization<br>SSL</div>
  <div class="tier-body" style="top:68px">
    <h3>High Assurance SSL</h3>
    <p>High assurance SSL with full organisation verification displays enhanced levels of trust and security.</p>
    <span class="learn-btn">Learn More</span>
  </div>
</section>

<section class="band band-ext">
  <svg class="notch" width="52" height="26" viewBox="0 0 52 26"><path d="M0 0 H52 L26 26 Z" fill="var(--org)"/></svg>
  <div class="tier-label" style="top:92px;color:var(--ext-label)">Extended<br>SSL</div>
  <div class="tier-body" style="top:70px">
    <h3>Activate the Green Address Bar!</h3>
    <p>The highest assurance level of website trust - visitors see the green bar and enhanced trust means enhanced sales. EV SSL is preferred by all major online brands.</p>
    <span class="learn-btn">Learn More</span>
  </div>
</section>

<section class="clients">
  <div class="client" style="left:253px">Hostbeam</div>
  <div class="client" style="left:488px"><span class="dot"></span>ShopKestrel</div>
  <div class="client" style="left:704px">Nextwire</div>
  <div class="client" style="left:944px">Queryheap</div>
</section>

<footer class="footer">
  <div class="mark">47certo</div>
  <div class="links">About<span>|</span>Contact Us<span>|</span>Products<span>|</span>Terms &amp; Conditions</div>
  <div class="copy">© 2013 47certo. All Rights Reserved.</div>
  <div class="contact">contact@47certo.com<br>1.555.010.4477</div>
  <div class="address">2140 Larkspur Ave. #310<br>Fenwick, CA 90412.</div>
</footer>

</body>
</html>
```